Painting Valtoni Renovations New buildings

Paint jobs plasterwork renovations new building customer painter paper drywall Entsorgungen.neukunden win color splash pleasure in colors competent clean fast reliable new try build demolition color combinations color concepts offers washing façade painting wood stains new projects old building renovations yes no beautiful new old sell secure solve paint over paint paint spray paint lye assemble disassemble sell buy trade oil dust new old assembly disassembly putty sanding fashion devastation copying belief feng shui kleopatra pompes beer colors swamp lime abrasion release tighten

Target Market(s)

construction industry

Contact Information for Business Card

Maler

Font styles to use
Serif

Colors
f04a50
959595

Requirements
Must have
• elegant appearance
Nice to have
• simply goal-oriented clientele in detail
Should not have
• too colorful

```html
<!DOCTYPE html>
<html lang="en">
<head>
<meta charset="utf-8">
<title>Corvella – Business Card</title>
<link href="https://fonts.googleapis.com/css2?family=Lora:ital,wght@0,400;0,700;1,700&display=swap" rel="stylesheet">
<style>
  :root {
    --backdrop: #2a2b2f;
    --card-blue: #1f4680;
    --card-white: #ffffff;
    --brand-blue: #1f4680;
    --accent-band: #6f86c4;
    --text-light: #ffffff;
    --text-soft: #dfe6f2;
  }
  html, body {
    margin: 0;
    padding: 0;
    width: 1200px;
    height: 800px;
    overflow: hidden;
    background: var(--backdrop);
  }
  .canvas {
    position: relative;
    width: 1200px;
    height: 800px;
  }
  .business-card {
    position: absolute;
    left: 180px;
    top: 160px;
    width: 840px;
    height: 480px;
    border-radius: 26px;
    overflow: hidden;
    box-shadow: 0 18px 40px rgba(0,0,0,0.45);
  }
  .card-art {
    position: absolute;
    inset: 0;
  }
  .brand {
    position: absolute;
    left: 70px;
    top: 205px;
    display: flex;
    align-items: center;
    gap: 14px;
  }
  .brand-dot {
    width: 26px;
    height: 26px;
    border-radius: 50%;
    background: var(--brand-blue);
  }
  .brand-name {
    font-family: "Lora", serif;
    font-weight: 700;
    font-size: 58px;
    color: var(--brand-blue);
    letter-spacing: 1px;
  }
  .contact {
    position: absolute;
    left: 545px;
    top: 92px;
    font-family: "Lora", serif;
    color: var(--text-light);
  }
  .contact-name {
    margin: 0;
    font-style: italic;
    font-weight: 700;
    font-size: 30px;
    line-height: 1.1;
  }
  .contact-role {
    margin: 2px 0 0;
    font-size: 17px;
    color: var(--text-soft);
  }
  .contact-address {
    margin: 26px 0 0;
    font-size: 17px;
    line-height: 1.35;
    font-style: normal;
    color: var(--text-soft);
  }
  .contact-list {
    list-style: none;
    margin: 24px 0 0;
    padding: 0;
    font-size: 17px;
  }
  .contact-list li {
    display: flex;
    align-items: center;
    gap: 10px;
    height: 28px;
  }
  .contact-icon {
    width: 20px;
    height: 20px;
    flex: none;
  }
</style>
</head>
<body>
<main class="canvas">
  <section class="business-card" aria-label="Business card for Corvella painters">
    <svg class="card-art" width="840" height="480" viewBox="0 0 840 480" role="img" aria-label="Blue card field with a large white circle, edged by a colour swoosh band">
      <rect class="card-field" width="840" height="480" fill="var(--card-blue)"/>
      <circle class="accent-band" cx="150" cy="330" r="370" fill="none" stroke="var(--accent-band)" stroke-width="12"/>
      <circle class="white-panel" cx="150" cy="330" r="362" fill="var(--card-white)"/>
    </svg>

    <div class="brand">
      <span class="brand-dot"></span>
      <span class="brand-name">Corvella</span>
    </div>

    <div class="contact">
      <h1 class="contact-name">Merenda Valtoni</h1>
      <p class="contact-role">Manager</p>
      <address class="contact-address">PO BOX 480, Linden Road<br>7th street Harwick</address>
      <ul class="contact-list">
        <li>
          <svg class="contact-icon" viewBox="0 0 20 20"><circle cx="10" cy="10" r="9" fill="#fff"/><rect x="6.5" y="5" width="7" height="10" rx="1.5" fill="none" stroke="#1f4680" stroke-width="1.6"/></svg>
          (555) 210 4471
        </li>
        <li>
          <svg class="contact-icon" viewBox="0 0 20 20"><circle cx="10" cy="10" r="9" fill="#fff"/><path d="M6.5 5.5c1-.6 1.6.1 2.2 1.3.4.8 0 1.2-.5 1.6.5 1.3 1.5 2.4 2.9 3 .4-.5.8-1 1.6-.6 1.2.6 1.9 1.2 1.3 2.2-.8 1.3-2.4 1.4-4.3.3-2-1.2-3.3-2.8-4-4.6-.5-1.5-.2-2.6.8-3.2z" fill="#1f4680"/></svg>
          (555) 210 4472
        </li>
        <li>
          <svg class="contact-icon" viewBox="0 0 20 20"><circle cx="10" cy="10" r="9" fill="#fff"/><rect x="5" y="6.5" width="10" height="7" rx="1" fill="#1f4680"/><path d="M5.5 7l4.5 3.5L14.5 7" fill="none" stroke="#fff" stroke-width="1"/></svg>
          info@corvellapaint.com
        </li>
        <li>
          <svg class="contact-icon" viewBox="0 0 20 20"><circle cx="10" cy="10" r="9" fill="#fff"/><circle cx="10" cy="10" r="5" fill="none" stroke="#1f4680" stroke-width="1.3"/><path d="M5 10h10M10 5c-2.5 3-2.5 7 0 10M10 5c2.5 3 2.5 7 0 10" fill="none" stroke="#1f4680" stroke-width="1"/></svg>
          www.corvellapaint.com
        </li>
      </ul>
    </div>
  </section>
</main>
</body>
</html>
```